Beacon Advisory Website

I currently have a website www.beaconadvisoryinc.example. We are a IT Consulting Company. Our website will pretty much tell out our services. I am looking to enhance my website and make it look more professional. Looking for very classy and Contemporary look and design for my website.

Industry/Entity Type

It Company

```html
<!DOCTYPE html>
<html lang="en">
<head>
<meta charset="utf-8">
<title>Beacon Advisory — IT & Management Consulting</title>
<link href="https://fonts.googleapis.com/css2?family=Raleway:wght@400;500;600;700&family=Open+Sans:wght@400;600;700&display=swap" rel="stylesheet">
<style>
:root{
  --brand:#1f6fbf;
  --brand-dark:#0d4f97;
  --brand-bright:#1a8fd8;
  --nav:#1565b8;
  --ink:#222;
  --muted:#777;
  --pale:#eef2f8;
  --line:#d7dde6;
  --white:#fff;
}
*{box-sizing:border-box;margin:0;padding:0}
html,body{width:1200px;height:3529px;overflow:hidden}
body{font-family:"Open Sans",Arial,sans-serif;color:var(--ink);background:var(--white);position:relative}
.wrap{width:910px;margin:0 auto;position:relative}
a{color:inherit;text-decoration:none}

/* header */
.topbar{height:85px}
.topbar .wrap{display:flex;justify-content:space-between;align-items:center;height:85px}
.brand{display:flex;align-items:center;gap:12px;font-family:"Raleway",sans-serif;font-weight:700;font-size:30px;color:var(--brand)}
.brand-mark{width:34px;height:34px;border-radius:50%;background:var(--brand)}
.talk{display:flex;align-items:center;gap:12px}
.talk-title{font-family:"Raleway",sans-serif;font-weight:700;font-size:21px;color:var(--brand)}
.talk-sub{font-size:11px;color:var(--muted)}
.nav{height:38px;background:linear-gradient(#1c74c8,#0f5aa8)}
.nav .wrap{display:flex;align-items:center;height:38px;gap:34px;font-size:12.5px;color:var(--white);font-weight:600}
.nav .search{margin-left:auto}

/* hero */
.hero{height:482px;position:relative;background:radial-gradient(ellipse at 70% 30%,#8fe0ff 0%,#2aa7e0 35%,#0b6fb8 75%,#06508f 100%);color:var(--white)}
.hero-copy{position:absolute;left:153px;top:142px;width:520px}
.hero h1{font-family:"Raleway",sans-serif;font-weight:500;font-size:30px;line-height:1.25;margin-bottom:14px}
.hero p{font-size:12px;line-height:1.55}
.dots{position:absolute;left:550px;top:430px;display:flex;gap:10px}
.dots span{width:17px;height:17px;border-radius:50%;background:var(--white)}

/* intro */
.section-title{font-family:"Raleway",sans-serif;text-align:center;color:#555}
.intro{height:576px;padding-top:50px}
.intro .section-title{font-size:24px;font-weight:700;color:#666}
.rule{width:100px;height:3px;background:var(--brand);margin:14px auto 0}
.lede{text-align:center;font-size:12px;color:var(--muted);margin-top:16px}
.features{display:flex;justify-content:space-between;margin-top:46px}
.feature{width:280px;text-align:center}
.feature svg{height:70px}
.feature h3{font-family:"Raleway",sans-serif;font-weight:700;font-size:20px;color:var(--brand);margin:4px 0 8px}
.feature p{font-size:11.5px;color:var(--muted);text-align:justify;line-height:1.45}
.feature .more{display:block;font-size:11.5px;margin-top:12px}
.attract{display:flex;justify-content:space-between;align-items:center;margin-top:52px}
.attract-text{width:460px}
.attract h4{font-family:"Raleway",sans-serif;font-weight:700;font-size:15.5px;line-height:1.35;margin-bottom:8px}
.attract p{font-size:11.5px;color:var(--muted);line-height:1.45}
.callbox{width:320px;height:84px;background:var(--pale);display:flex;align-items:center;gap:14px;padding:0 18px}

/* services */
.services{height:524px;background:var(--pale);padding-top:45px}
.services h2{font-family:"Raleway",sans-serif;font-weight:400;font-size:28px;color:#444}
.svc-grid{display:grid;grid-template-columns:repeat(3,280px);justify-content:space-between;row-gap:38px;margin-top:28px}
.svc h3{display:flex;align-items:center;gap:8px;font-family:"Raleway",sans-serif;font-weight:500;font-size:16px;color:#444;margin-bottom:8px;height:34px}
.svc p{font-size:11.5px;color:var(--muted);line-height:1.45}
.cta-line{display:flex;align-items:center;margin-top:50px;font-family:"Raleway",sans-serif}
.cta-line strong{color:var(--brand);font-size:17px;margin-right:14px}
.cta-line span{font-size:16px;font-weight:500}
.btn-outline{margin-left:auto;border:2px solid var(--brand);color:var(--brand);font-size:13px;padding:8px 30px}

/* process */
.process{height:515px;position:relative;background:linear-gradient(90deg,#0e4f9a 0%,#1565b8 45%,#2d7fc6 100%);color:var(--white)}
.process-photo{position:absolute;right:0;top:0;width:610px;height:515px;background:linear-gradient(90deg,rgba(21,101,184,0) 0%,#7faed9 35%,#c9dced 70%,#9bbede 100%)}
.process-copy{position:absolute;left:170px;top:148px;width:400px}
.process h2{font-family:"Raleway",sans-serif;font-weight:400;font-size:34px;margin-bottom:26px}
.process p{font-size:11.5px;line-height:1.5}
.btn-ghost{display:inline-block;border:1px solid rgba(255,255,255,.7);font-size:11px;padding:9px 30px;margin-top:26px}
.process .phone{font-family:"Raleway",sans-serif;font-size:17px;margin-top:22px}

/* solutions */
.solutions{height:666px;position:relative;padding-top:40px}
.solutions h2{font-family:"Raleway",sans-serif;font-weight:400;font-size:29px;color:#444;text-align:center}
.sol-photo{position:absolute;left:0;top:166px;width:567px;height:425px;background:linear-gradient(120deg,#f4f4f4 0%,#e2e4e8 50%,#f6f6f6 100%)}
.sol-list{position:absolute;left:609px;top:186px;width:420px}
.sol-item{margin-bottom:34px}
.sol-item h3{display:flex;align-items:center;gap:10px;font-family:"Raleway",sans-serif;font-weight:500;font-size:17px;color:var(--brand);margin-bottom:8px}
.sol-item p{font-size:11.5px;color:var(--muted);line-height:1.45}
.sol-item .more{display:block;font-size:11.5px;font-weight:700;margin-top:12px}

/* careers */
.careers{height:189px;position:relative;background:linear-gradient(90deg,#1771c2,#4d98d6 50%,#2c80c8);color:var(--white)}
.careers .wrap{display:flex;align-items:center;height:189px}
.careers h2{font-family:"Raleway",sans-serif;font-weight:700;font-size:30px}
.careers p{font-size:13px}
.btn-solid{margin-left:115px;background:var(--brand-dark);font-size:12.5px;padding:12px 42px}

/* footer */
.footer{height:355px;padding-top:68px}
.footer .wrap{display:flex}
.fcol{font-size:11.5px;color:var(--muted);line-height:1.6}
.fcol h4{font-family:"Raleway",sans-serif;font-weight:500;font-size:15px;color:var(--brand);margin-bottom:8px}
.fcol b{color:#333;font-weight:600}
.fcol .gap{margin-top:18px}
.c1{width:217px;margin-left:25px}.c2{width:199px}.c3{width:234px}.c4{width:235px}
.field{display:flex;justify-content:space-between;align-items:center;border-bottom:1px solid var(--line);padding:4px 0;margin-top:14px;width:190px}
.btn-sub{display:inline-block;background:var(--brand-dark);color:var(--white);font-size:11px;padding:2px 14px;margin-top:8px}
.social{display:flex;gap:6px;margin-top:6px}
.social span{width:20px;height:20px;background:#333}
.bottom{position:absolute;left:145px;top:3430px;width:910px;border-top:1px solid var(--line);display:flex;justify-content:space-between;padding-top:28px;font-size:11.5px;color:var(--muted)}
.bottom .links{display:flex;gap:30px}
.bottom .name{color:var(--brand)}
</style>
</head>
<body>

<header class="topbar">
  <div class="wrap">
    <a class="brand" href="#"><span class="brand-mark"></span>Beacon Advisory</a>
    <div class="talk">
      <svg width="52" height="52" viewBox="0 0 52 52" fill="none" stroke="#1f6fbf" stroke-width="3"><circle cx="26" cy="26" r="23"/><path d="M15 28v-4a11 11 0 0 1 22 0v4"/><rect x="12" y="26" width="6" height="9" rx="2"/><rect x="34" y="26" width="6" height="9" rx="2"/></svg>
      <div><div class="talk-title">Talk With Us: +1 (555) 014 2290</div><div class="talk-sub">Let us help you determine the best fit for your needs</div></div>
    </div>
  </div>
</header>

<nav class="nav">
  <div class="wrap">
    <a href="#">HOME</a><a href="#">COMPANY</a><a href="#">SERVICES</a><a href="#">SOLUTIONS</a><a href="#">RESOURCES</a><a href="#">CAREER</a><a href="#">CONTACT US</a>
    <svg class="search" width="16" height="16" viewBox="0 0 16 16" fill="none" stroke="#fff" stroke-width="2"><circle cx="6.5" cy="6.5" r="5"/><path d="M10.5 10.5l4 4"/></svg>
  </div>
</nav>

<section class="hero" role="img" aria-label="Bright blue background with soft glowing light spots">
  <div class="hero-copy">
    <h1>Expert Qualified IT &amp; Management Professionals</h1>
    <p>Today's IT market is a dynamic, fast-paced industry, with ever-increasing demands. Meeting these demands for over 25 years, Beacon Advisory maintains a global presence, aggressively recruiting expertly qualified</p>
  </div>
  <div class="dots"><span></span><span></span><span></span></div>
</section>

<section class="intro">
  <div class="wrap">
    <h2 class="section-title">Today's IT market is a dynamic, fast-paced industry</h2>
    <div class="rule"></div>
    <p class="lede">Lorem Ipsum is simply dummy text of the printing and typesetting industry.</p>
    <div class="features">
      <div class="feature">
        <svg viewBox="0 0 90 70" width="90" fill="none" stroke="#1f6fbf" stroke-width="2.5"><rect x="4" y="6" width="52" height="34" rx="4"/><path d="M14 40v12l12-12"/><rect x="34" y="24" width="50" height="32" rx="4" fill="#fff"/><path d="M72 56v10l-10-10"/></svg>
        <h3>Consulting</h3>
        <p>Beacon Advisory has certified professional consultants to work with you to help increase the business by providing IT services...</p>
        <a class="more" href="#">Read More</a>
      </div>
      <div class="feature">
        <svg viewBox="0 0 90 70" width="90" fill="#1f6fbf"><circle cx="45" cy="18" r="9"/><path d="M32 60v-18a13 13 0 0 1 26 0v18z"/><circle cx="22" cy="26" r="7"/><path d="M12 62v-14a10 10 0 0 1 20 0v14z"/><circle cx="68" cy="26" r="7"/><path d="M58 62v-14a10 10 0 0 1 20 0v14z"/></svg>
        <h3>Staff Augmentation</h3>
        <p>For years Beacon Advisory has been offering our customers the ability to augment their existing staff</p>
        <a class="more" href="#">Read More</a>
      </div>
      <div class="feature">
        <svg viewBox="0 0 90 70" width="90" fill="none" stroke="#1f6fbf" stroke-width="2.5"><circle cx="45" cy="30" r="20"/><circle cx="45" cy="30" r="8"/><path d="M45 6v8M45 46v8M21 30h8M61 30h8M28 13l6 6M56 41l6 6M62 13l-6 6M34 41l-6 6"/><path d="M20 62c8-5 17 5 25 0s17-5 25 0"/></svg>
        <h3>Offshore</h3>
        <p>Our Offshore development model has a unique distinction of providing efficient software solutions</p>
        <a class="more" href="#">Read More</a>
      </div>
    </div>
    <div class="attract">
      <div class="attract-text">
        <h4>Attracting and developing the best talent for our business, stretching our people and developing a "can do" attitude.</h4>
        <p>Beacon Advisory has been governed by its core values. They shape the culture and define the character of our company. They guide how we behave and make decisions.</p>
      </div>
      <div class="callbox">
        <svg width="52" height="52" viewBox="0 0 52 52" fill="none" stroke="#1f6fbf" stroke-width="3"><circle cx="26" cy="26" r="23"/><path d="M15 28v-4a11 11 0 0 1 22 0v4"/><rect x="12" y="26" width="6" height="9" rx="2"/><rect x="34" y="26" width="6" height="9" rx="2"/></svg>
        <div><div class="talk-title" style="font-size:17px">Talk With Us: +1 (555) 014 2290</div><div class="talk-sub" style="font-size:9.5px">Let us help you determine the best fit for your needs</div></div>
      </div>
    </div>
  </div>
</section>

<section class="services">
  <div class="wrap">
    <h2>Our Services</h2>
    <div class="svc-grid">
      <div class="svc"><h3><svg width="30" height="30" viewBox="0 0 30 30" fill="none" stroke="#333" stroke-width="1.8"><circle cx="15" cy="8" r="4"/><path d="M15 12v10M5 26h20M8 22l7-4 7 4"/></svg>Technology</h3><p>Beacon Advisory has been governed by its core values. They shape the culture and define the character of our company. They guide how we behave and make decisions.</p></div>
      <div class="svc"><h3><svg width="30" height="30" viewBox="0 0 30 30" fill="none" stroke="#333" stroke-width="1.8"><circle cx="15" cy="12" r="8"/><circle cx="15" cy="12" r="3"/><path d="M6 25c3-2 6 2 9 0s6-2 9 0"/></svg>Offshore</h3><p>Beacon Advisory has been governed by its core values. They shape the culture and define the character of our company. They guide how we behave and make decisions.</p></div>
      <div class="svc"><h3><svg width="30" height="30" viewBox="0 0 30 30" fill="none" stroke="#333" stroke-width="1.8"><rect x="4" y="4" width="16" height="14" rx="2"/><rect x="12" y="12" width="14" height="14" rx="2" fill="#eef2f8"/><path d="M16 17h6M16 21h6"/></svg>Application Developement</h3><p>Beacon Advisory has been governed by its core values. They shape the culture and define the character of our company. They guide how we behave and make decisions.</p></div>
      <div class="svc"><h3><svg width="30" height="30" viewBox="0 0 30 30" fill="none" stroke="#333" stroke-width="1.8"><ellipse cx="15" cy="7" rx="9" ry="3"/><path d="M6 7v12c0 2 4 3 9 3s9-1 9-3V7M6 13c0 2 4 3 9 3s9-1 9-3"/><path d="M10 27h10"/></svg>Enterprise Integration</h3><p>Beacon Advisory has been governed by its core values. They shape the culture and define the character of our company. They guide how we behave and make decisions.</p></div>
      <div class="svc"><h3><svg width="30" height="30" viewBox="0 0 30 30" fill="none" stroke="#333" stroke-width="2"><path d="M4 24l8-8 5 5 9-12M20 9h6v6"/></svg>IT Consulting</h3><p>Beacon Advisory has been governed by its core values. They shape the culture and define the character of our company. They guide how we behave and make decisions.</p></div>
      <div class="svc"><h3>Technology</h3><p>Beacon Advisory has been governed by its core values. They shape the culture and define the character of our company. They guide how we behave and make decisions.</p></div>
    </div>
    <div class="cta-line">
      <strong>Talk With Us: +1 (555) 014 2290 -</strong>
      <span>Our Sales Specialist can help you decide</span>
      <a class="btn-outline" href="#">CONTACT US</a>
    </div>
  </div>
</section>

<section class="process">
  <div class="process-photo" role="img" aria-label="Photo of two business colleagues reviewing a tablet together"></div>
  <div class="process-copy">
    <h2>Our Processs</h2>
    <p>We bring together seasoned IT executives and battle-tested computer support personnel, provide them with the right resources for the job, immerse them in a collaborative and dynamic culture, and push them to their limits. We also provide plenty of caffeine.</p>
    <a class="btn-ghost" href="#">READ MORE</a>
    <div class="phone">Talk With Us: +1 (555) 014 2290</div>
  </div>
</section>

<section class="solutions">
  <h2>Our Solutions</h2>
  <div class="rule" style="width:0;height:0"></div>
  <p class="lede" style="margin-top:28px">Lorem Ipsum is simply dummy text of the printing and typesetting industry.</p>
  <div class="sol-photo" role="img" aria-label="Photo of a man at a laptop beside a maze with a red path through it"></div>
  <div class="sol-list">
    <div class="sol-item">
      <h3><svg width="20" height="18" viewBox="0 0 20 18" fill="#1f6fbf"><rect x="1" y="1" width="18" height="12" rx="1"/><rect x="7" y="14" width="6" height="3"/></svg>Dashboard</h3>
      <p>Dashboards are a key component of every organization's Performance Management and Business Transformation initiatives. They provide a simple, intuitive and effective means to monitor performance using visual charts</p>
      <a class="more" href="#">READ MORE</a>
    </div>
    <div class="sol-item">
      <h3><svg width="20" height="18" viewBox="0 0 20 18" fill="#1f6fbf"><path d="M5 15a4 4 0 0 1 0-8 6 6 0 0 1 11 1 3.5 3.5 0 0 1 0 7z"/></svg>Data Warehousing</h3>
      <p>A data warehouse is the concept of data extracted from operational systems and made available as historical snapshots for ad-hoc queries and scheduled reporting</p>
      <a class="more" href="#">READ MORE</a>
    </div>
    <div class="sol-item">
      <h3><svg width="20" height="18" viewBox="0 0 20 18" fill="#1f6fbf"><circle cx="7" cy="7" r="5"/><circle cx="15" cy="13" r="4"/></svg>BPM</h3>
      <p>Beacon Advisory having Flowline Certified Consultants in to provide Business Process Management capabilities to our clients. We help businesses to build for change with a new kind of software that lets business users directly capture their business goals</p>
      <a class="more" href="#">READ MORE</a>
    </div>
  </div>
</section>

<section class="careers" role="img" aria-label="Blue-tinted photo of an open office with staff at work">
  <div class="wrap">
    <div>
      <h2>Careers</h2>
      <p>We appreciate your interest in exploring career opportunities with us.</p>
    </div>
    <a class="btn-solid" href="#">APPLY NOW</a>
  </div>
</section>

<footer class="footer">
  <div class="wrap">
    <div class="fcol c1"><h4>Services</h4>Technology<br>Business<br>Application Development<br>Enterprise Integration<br>IT Consulting</div>
    <div class="fcol c2"><h4>Solutions</h4>Dashboard<br>Data Warehousing<br>BPM<h4 class="gap">Resources</h4>Our Process<br>Staff Augmentation</div>
    <div class="fcol c3"><h4>Contact Us</h4><b>Head Office</b><br>410 Harbor Lane Suite 210<br>Westfield, NJ 07090<br>Phone: +1 (555) 014 2290<div class="gap"><b>Technical Center</b><br>2200 Maple Ridge Road Suite 120<br>Lakeview MI 48850</div><div class="gap"><b>West Coast Office</b><br>1870 Summit Plaza Suite 400<br>Fairview, CA 95020</div></div>
    <div class="fcol c4"><h4>Newsletter</h4>Subscribe with us to get the latest news and updates
      <div class="field"><span>Enter email</span><svg width="10" height="10" viewBox="0 0 10 10" fill="#333"><path d="M0 5l10-5-4 10-1-4z"/></svg></div>
      <span class="btn-sub">SUBMIT</span>
      <h4 class="gap">Connect With Us</h4>
      <div class="social"><span></span><span></span><span></span></div>
    </div>
  </div>
</footer>

<div class="bottom">
  <div>Copyright 2016 <span class="name">Beacon Advisory</span>. All Rights Reserved</div>
  <div class="links"><a href="#">Home</a><a href="#">Terms &amp; Conditions</a><a href="#">Privacy Policy</a><a href="#">Sitemap</a></div>
</div>

</body>
</html>
```